Residential Real Estate needs a flyer design

I need a flyer that brings all my companies together to target that person who needs to sell, rent, or refinance their home. We specialize in buying, selling, managing, and providing home loans in El Paso, TX. I have uploaded a document that will give you all my thoughts of this flyer. My companies include Brisk Mortgage Lending (Residential Mortgage Lending), Tallow Realty El Paso (Real Estate Brokerage), Quill Lease Homes El Paso (Property Management Company), MVT Capital, LLC (Real Estate Investment Manager). I believe home owners need more options in the residential real estate market. Most real estate companies can only sell a home - we can sell, rent, manage, buy or refinance a home. We have the ability to put your home on the market for sale and rent at the same time, which gives you two options at once. We also buy homes as investments (MVT Capital, LLC). All homes purchased are cash buys and can close in 10 days. We specialize in the residential real estate market in El Paso, TX (selling & buying), mortgage lending, and the property management business. Our evaluation is completely free of charge. All companies are under the same management and broker. We have a few thing we use in marketing: 1. We will sell your home in 60 days, or we will buy it....Guaranteed in writing. 2. We will sell your home in 60 days, or we will sell it for free....Guaranteed in writing. 3. We will provide you with an offer to buy your home in 24 hours guaranteed. 4. We will rent your home in 60 days, or we will manage it for free for 1 month. HOW ARE WE DIFFERENT? We are able to provide you with every possible option and educate you in each scenario with guarantees.

Target Market(s)

Expired Listings

Industry/Entity Type

Real Estate

Font styles to use
Serif

Requirements
Must have
• *Certain Restrictions Apply – Call For Details.
• This is not intended to be a solicitation if your home is currently listed with a broker.

```html
<!DOCTYPE html>
<html lang="en">
<head>
<meta charset="utf-8">
<title>Homes Purchased – Flyer Back</title>
<link rel="stylesheet" href="https://fonts.googleapis.com/css2?family=Merriweather:wght@400;700;900&family=Open+Sans:wght@400;600&display=swap">
<style>
  :root {
    --stage: #9d9d9d;
    --band-dark: #474747;
    --orange: #f7941d;
    --heading-orange: #f39a1e;
    --red: #b21f24;
    --deep-red: #a51c20;
    --ink: #1a1a1a;
    --paper-top: #ffffff;
    --paper-bottom: #bdbdbd;
    --blue: #29a9e0;
    --yellow: #f5d311;
    --magenta: #d8176b;
    --green: #6fbf3f;
    --logo-green: #2f9a45;
  }
  * { margin: 0; padding: 0; box-sizing: border-box; }
  html, body { width: 1200px; height: 1000px; overflow: hidden; }
  body { background: var(--stage); position: relative; font-family: "Merriweather", Georgia, serif; }

  .flyer {
    position: absolute; left: 320px; top: 25px; width: 712px; height: 920px;
    background: linear-gradient(180deg, var(--paper-top) 0%, #ededed 40%, var(--paper-bottom) 100%);
    box-shadow: 4px 6px 12px rgba(0,0,0,.45);
    overflow: hidden;
  }
  .section-band { position: absolute; left: 0; width: 712px; height: 62px; }
  .section-band svg { position: absolute; left: 0; top: 0; }
  .section-title {
    position: absolute; left: 20px; color: var(--heading-orange);
    font-weight: 700; white-space: nowrap;
  }
  .band-purchased { top: 14px; }
  .band-purchased .section-title { top: 17px; font-size: 22px; }
  .band-different { top: 423px; }
  .band-different .section-title { top: 15px; font-size: 23px; letter-spacing: .3px; }

  .intro { position: absolute; left: 20px; top: 93px; font-size: 12.5px; color: var(--ink); }

  .homes-box {
    position: absolute; left: 17px; top: 141px; width: 678px; height: 269px;
    background: #fff; border: 2px solid var(--red); border-radius: 2px;
    box-shadow: 2px 3px 6px rgba(0,0,0,.35);
  }
  .homes-col { position: absolute; top: 23px; list-style: none;
    font-family: "Open Sans", Arial, sans-serif; font-size: 10.5px; line-height: 16.4px; color: var(--ink); }
  .homes-col.c1 { left: 24px; } .homes-col.c2 { left: 253px; } .homes-col.c3 { left: 480px; }

  .lead { position: absolute; left: 17px; top: 492px; font-size: 14.5px; font-weight: 700; color: var(--ink); }
  .guarantees { position: absolute; left: 20px; top: 526px; list-style: none; }
  .guarantees li { position: relative; height: 31.3px; padding-left: 22px;
    font-size: 12.3px; font-weight: 700; color: var(--deep-red); }
  .guarantees svg { position: absolute; left: 0; top: 3px; }

  .partners {
    position: absolute; left: 15px; top: 675px; width: 683px; height: 143px;
    background: #fff; border: 2px solid var(--orange); border-radius: 16px;
    box-shadow: 1px 2px 5px rgba(0,0,0,.3);
  }
  .partner { position: absolute; display: flex; align-items: center; gap: 8px;
    font-family: "Merriweather", Georgia, serif; white-space: nowrap; }
  .partner .mark { display: inline-block; width: 14px; height: 14px; }
  .partner-capital { left: 26px; top: 62px; font-size: 15px; color: var(--logo-green); }
  .partner-capital .mark { background: var(--logo-green); border-radius: 50%; }
  .partner-lease { left: 236px; top: 54px; flex-direction: column; align-items: flex-start; gap: 2px; color: #111; }
  .partner-lease .name { font-size: 16px; font-weight: 700; }
  .partner-lease .tag { font-size: 8.5px; }
  .partner-mortgage { left: 510px; top: 38px; flex-direction: column; align-items: center; gap: 4px; color: #222; }
  .partner-mortgage .mark { width: 22px; height: 22px; background: #1c2b22; border-radius: 50%; }
  .partner-mortgage .name { font-size: 14px; }
  .partner-mortgage .url { font-size: 7.5px; }

  .footer-red { position: absolute; left: 0; top: 833px; width: 712px; height: 14px; background: var(--red); }
  .footer { position: absolute; left: 0; top: 847px; width: 712px; height: 73px; background: var(--orange); text-align: center; }
  .footer .note { margin-top: 10px; font-size: 12px; color: #222; }
  .footer .address { margin-top: 8px; font-size: 14px; font-weight: 700; color: #fff; }
</style>
</head>
<body>
<main class="flyer">

  <header class="section-band band-purchased">
    <svg width="712" height="62" viewBox="0 0 712 62">
      <polygon points="0,6 470,6 488,34 470,58 0,58" fill="var(--band-dark)"/>
      <rect x="0" y="6" width="470" height="2" fill="var(--orange)"/>
      <polygon points="458,2 498,2 530,34 498,66 458,66 490,34" fill="#fff" stroke="#9a9a9a" stroke-width="1" transform="scale(1,0.88)"/>
      <polygon points="506,2 532,2 564,34 532,66 506,66 538,34" fill="#fff" stroke="#9a9a9a" stroke-width="1" transform="scale(1,0.88)"/>
      <polygon points="490,6 500,6 520,30 500,52 490,52 510,30" fill="var(--band-dark)"/>
    </svg>
    <h1 class="section-title">Homes Purchased this year (2014)</h1>
  </header>

  <p class="intro">All homes purchased in this program by our investors are used for rental purposes.</p>

  <section class="homes-box" aria-label="Homes purchased in 2014">
    <ol class="homes-col c1">
      <li>1. 10769 Willow Crest ($91,000)</li>
      <li>4. 12849 Harmony ($120,000)</li>
      <li>7. 7248 Amber Stone ($100,000)</li>
      <li>10. 11876 Copper Dune ($86,500)</li>
      <li>13. 3100 Sierra Azul ($167,500)</li>
      <li>16. 792 Canyon Wind ($86,800)</li>
      <li>19. 12061 Luis Medina ($95,000)</li>
      <li>22. 11513 Pablo Ortega ($150,000)</li>
      <li>25. 753 Dry Sage ($84,000)</li>
      <li>28. 11103 Red Rock Cove ($121,500)</li>
      <li>31. 12360 Sierra Vista ($81,000)</li>
      <li>34. 14283 Ranchos Rock ($101,550)</li>
      <li>37. 12636 Sun Crest ($157,000)</li>
      <li>40. 10744 Pleasant Dune ($125,000)</li>
    </ol>
    <ol class="homes-col c2">
      <li>2. 12716 Sierra Alta ($120,000)</li>
      <li>5. 536 Camino Del Roble ($218,000)</li>
      <li>8. 11512 Henry Walsh ($178,000)</li>
      <li>11. 10945 Mesa Verde ($118,000)</li>
      <li>14. 11601 Still Water ($83,000)</li>
      <li>17. 11969 Tom Hardin ($86,000)</li>
      <li>20. 12844 Sierra Luna ($105,320)</li>
      <li>23. 10529 Silverbrook ($85,000)</li>
      <li>26. 12576 Rosa Blanca ($84,362)</li>
      <li>29. 304 Sam Keller ($80,000)</li>
      <li>32. 444 Yucca Crossing ($85,000)</li>
      <li>35. 6243 Ibex Circle ($68,298)</li>
      <li>38. 11437 Pinos Navarro ($138,500)</li>
    </ol>
    <ol class="homes-col c3">
      <li>3. 3128 Falcon Ridge ($162,500)</li>
      <li>6. 3256 Oak Point ($98,404)</li>
      <li>9. 5541 Marco Reyes ($147,500)</li>
      <li>12. 3136 Sierra Roble ($92,000)</li>
      <li>15. 14185 Sierra Paloma ($86,000)</li>
      <li>18. 11237 Southridge ($152,000)</li>
      <li>21. 501 Calle De Sol ($119,000)</li>
      <li>24. 3261 Jade Point ($107,660)</li>
      <li>27. 14272 Desert Glow ($80,426)</li>
      <li>30. 6268 Caballero ($157,000)</li>
      <li>33. 5557 Marco Reyes ($149,000)</li>
      <li>36. 7904 Dusk Fall ($108,000)</li>
      <li>39. 1345 Tito Herrera ($143,500)</li>
    </ol>
  </section>

  <header class="section-band band-different">
    <svg width="712" height="62" viewBox="0 0 712 62">
      <polygon points="0,6 470,6 488,34 470,58 0,58" fill="var(--band-dark)"/>
      <polygon points="458,2 498,2 530,34 498,66 458,66 490,34" fill="#fff" stroke="#9a9a9a" stroke-width="1" transform="scale(1,0.88)"/>
      <polygon points="506,2 532,2 564,34 532,66 506,66 538,34" fill="#fff" stroke="#9a9a9a" stroke-width="1" transform="scale(1,0.88)"/>
      <polygon points="490,6 500,6 520,30 500,52 490,52 510,30" fill="var(--band-dark)"/>
    </svg>
    <h2 class="section-title">HOW ARE WE DIFFERENT?</h2>
  </header>

  <p class="lead">We are able to provide you with every possible option and educate you in each scenario.</p>

  <ul class="guarantees">
    <li><svg width="16" height="12"><polygon points="8,1 15,11 1,11" fill="var(--blue)"/></svg>We will sell your home in 60 days, or we will buy it....Guaranteed in writing.</li>
    <li><svg width="16" height="12"><polygon points="8,1 15,11 1,11" fill="var(--yellow)"/></svg>We will sell your home in 60 days, or we will sell it for free....Guaranteed in writing.</li>
    <li><svg width="16" height="12"><polygon points="1,2 15,2 8,11" fill="var(--magenta)"/></svg>We will provide you with an offer to buy your home in 24 hours guaranteed.</li>
    <li><svg width="16" height="12"><polygon points="1,2 15,2 8,11" fill="var(--green)"/></svg>We will rent your home in 60</li>
  </ul>

  <section class="partners" aria-label="Our companies">
    <div class="partner partner-capital"><span class="mark"></span><span>MVT Capital LLC</span></div>
    <div class="partner partner-lease">
      <span class="name">Quill Lease Homes</span>
      <span class="tag">El Paso Property Management &amp; Rental Services</span>
    </div>
    <div class="partner partner-mortgage">
      <span class="mark"></span>
      <span class="name">Brisk Mortgage Lending</span>
      <span class="url">www.BriskMortgageLending.com</span>
    </div>
  </section>

  <div class="footer-red"></div>
  <footer class="footer">
    <p class="note">Note: This is not intended to be a solicitation if your home is currently listed with a broker.</p>
    <p class="address">418 N. Cedar Ridge, B-2 El Paso, TX 79912</p>
  </footer>
</main>
</body>
</html>
```